Marquise Velvet Stable Goods - Elite line of horse care grooming products

I wanted to have a label design for my equestrian products that made the people who use them on their horses feel like a princess. I use all natural ingredients, they smell wonderful and work! I think my current design could be more amazing.... I have a total of 6 products. The final design should communicate that you are using the finest and highest quality ingredients on your best friend. please see my website (www.MarquiseStable.example) for the design aesthetic I'm going for. Design Guide:
The design should communicate that you are using the finest and highest quality ingredients on your best friend.
Create a bold, unique, visually-appealing design
Make buyer feel like a princess
Impart that you are taking care of your horse because you’re buying the best
Stand out from most other products currently on the market that look boring/outdated, bland
Avoid any design or visual images that impart chemical, industrial or commercial connotations
Key Terms: Elite, Bold, Serious, Baroque elegance, Feminine, Elegance, Wow, Fairytale, Fantasy, Elegance,

Please create: Design separate front and back BOPP labels for 32oz. spray bottle, 3.5x5” Rosemary, Lavender & Mint Insect Repellent

Design should convey a sense of wealth and prestige
Elegance & sophistication
Professional quality

Design Guide:

Key Attributes of Product:
Expensive product
Therapeutic-grade essential oils
All-natural ingredients
No poisons or pesticides
Smell wonderful
They work

Please use royal purple and gold

Target Market(s)

High end female horse owners..12-65yo female horse owners who want to and can afford to buy premium products for horse grooming.

Font styles to use
Sans Serif
Decorative
Script

Colors
876aae

Requirements
Must have
• Elegance, wow, pick me. Mandatory Graphics:
• Marquise Velvet Stable Goods logo with gold doily (no gradient on gold)
Nice to have
• Fairytale, fantasy, quality, elite, smells good,
Should not have
• I do not want my bottles to look like pesticides or poison.

```html
<!DOCTYPE html>
<html lang="en">
<head>
<meta charset="utf-8">
<title>Marquise Velvet Stable Goods – Natural Insect Repellent Label</title>
<link href="https://fonts.googleapis.com/css2?family=Montserrat:wght@500;600&family=Playball&family=Dancing+Script:wght@700&display=swap" rel="stylesheet">
<style>
  :root {
    --royal-purple: #6a2a8a;
    --deep-purple: #4f1f73;
    --ink-purple: #5b2d86;
    --gold: #c9a25a;
    --gold-light: #f3dcae;
    --gold-band: #cfc18a;
    --lavender: #8f72b8;
    --lavender-soft: #c9b7df;
    --white: #ffffff;
    --edge: #cfcfcf;
  }
  * { margin: 0; padding: 0; box-sizing: border-box; }
  html, body { width: 840px; height: 1200px; overflow: hidden; background: var(--white); }
  .label {
    position: relative;
    width: 840px;
    height: 1200px;
    background: var(--white);
    border: 1px solid var(--edge);
    overflow: hidden;
    font-family: "Montserrat", Arial, sans-serif;
  }
  .label-shapes { position: absolute; inset: 0; width: 840px; height: 1200px; }
  .brand-name {
    position: absolute;
    left: 540px; top: 210px;
    width: 240px;
    text-align: center;
    font-family: "Montserrat", Arial, sans-serif;
    font-weight: 600;
    font-size: 26px;
    line-height: 1.2;
    color: var(--ink-purple);
  }
  .title {
    position: absolute;
    left: 150px; width: 690px;
    text-align: center;
    font-family: "Playball", "Dancing Script", cursive;
    color: var(--gold-light);
    background: linear-gradient(180deg, #f8e4bb 0%, #d9ab6a 60%, #b8874a 100%);
    -webkit-background-clip: text;
    background-clip: text;
    -webkit-text-fill-color: transparent;
    text-shadow: none;
  }
  .title-main { top: 455px; font-size: 130px; line-height: 1.1; }
  .title-sub { top: 615px; font-size: 80px; line-height: 1.1; }
  .blend-band {
    position: absolute;
    left: 0; top: 751px;
    width: 840px; height: 91px;
    background: var(--gold-band);
    display: flex; align-items: center; justify-content: center;
    font-weight: 500;
    font-size: 33px;
    letter-spacing: 0.5px;
    color: var(--ink-purple);
  }
  .product-copy {
    position: absolute;
    left: 60px; top: 858px;
    width: 720px;
    text-align: center;
    font-weight: 500;
    font-size: 28px;
    line-height: 1.3;
    color: var(--white);
  }
  .slogan {
    position: absolute;
    left: 0; top: 1075px;
    width: 840px;
    text-align: center;
    font-family: "Dancing Script", cursive;
    font-weight: 700;
    font-size: 78px;
    line-height: 1.1;
    color: var(--ink-purple);
  }
  .slogan .small { font-size: 50px; }
</style>
</head>
<body>
<div class="label">
  <svg class="label-shapes" viewBox="0 0 756 1080" preserveAspectRatio="none" aria-hidden="false">
    <defs>
      <linearGradient id="purpleField" x1="0" y1="0" x2="1" y2="1">
        <stop offset="0" stop-color="#7a2e8e"/>
        <stop offset="1" stop-color="#4f1f73"/>
      </linearGradient>
      <linearGradient id="goldEdge" x1="0" y1="0" x2="1" y2="0">
        <stop offset="0" stop-color="#b8874a"/>
        <stop offset="0.5" stop-color="#f3dcae"/>
        <stop offset="1" stop-color="#b8874a"/>
      </linearGradient>
      <linearGradient id="lavenderTone" x1="0" y1="0" x2="0" y2="1">
        <stop offset="0" stop-color="#8f72b8"/>
        <stop offset="0.8" stop-color="#c9b7df"/>
        <stop offset="1" stop-color="#9aae8a"/>
      </linearGradient>
    </defs>

    <!-- purple field -->
    <path class="purple-field" fill="url(#purpleField)"
      d="M470,0 C400,60 390,250 270,410 C200,505 100,560 0,575 L0,945 C220,975 520,975 756,935 L756,0 Z"/>
    <!-- gold swoosh edges -->
    <path fill="none" stroke="url(#goldEdge)" stroke-width="6"
      d="M470,0 C400,60 390,250 270,410 C200,505 100,560 0,575"/>
    <path fill="none" stroke="url(#goldEdge)" stroke-width="6"
      d="M0,945 C220,975 520,975 756,935"/>

    <!-- logo medallion -->
    <circle cx="600" cy="225" r="192" fill="var(--white)" stroke="url(#goldEdge)" stroke-width="6"/>
    <circle cx="600" cy="225" r="170" fill="none" stroke="#d9c08a" stroke-width="30" opacity="0.55"
      role="img" aria-label="Gold lace doily frame around the brand medallion"/>
    <circle cx="600" cy="225" r="128" fill="var(--white)" stroke="#c9a25a" stroke-width="3"/>

    <!-- lavender sprigs area -->
    <rect x="62" y="30" width="130" height="460" rx="60" fill="url(#lavenderTone)" opacity="0.85"
      role="img" aria-label="Photograph of two lavender flower sprigs"/>
  </svg>

  <div class="brand-name">Marquise Velvet Stable Goods</div>

  <div class="title title-main">Natural</div>
  <div class="title title-sub">Insect Repellent</div>

  <div class="blend-band">LAVENDER, MINT &amp; ROSEMARY BLEND</div>

  <p class="product-copy">Natural ingredients made with therapeutic grade essential oils! Free of harsh chemicals, lovely smell. Safe for humans too...go ahead, spray it on yourself!</p>

  <div class="slogan">Love <span class="small">your</span> horse!</div>
</div>
</body>
</html>
```